Business card, postcard, pocket folder

We are a real estate team and have had a new logo designed. From this, we need the following deliverables:- Business Cards (double-sided)- Just Listed / Just Sold Postcards (double-sided)- Pocket Folder. See logo attached.More work possible for the winning designer.
There are 5 members of the team, so head shots should be easily changed and possible for a group photo might be a good idea for the pocket folder but not 100% neccessary.
Target Market(s)
Real estate
Industry/Entity Type
Real Estate
Font styles to use
Serif
Sans Serif
Requirements
Must have
- Business cards and postcards must have a head shot on them.

```html
<!DOCTYPE html>
<html lang="en">
<head>
<meta charset="utf-8">
<title>Harbrook Group – Stationery Set</title>
<link href="https://fonts.googleapis.com/css2?family=Roboto:wght@400;500;700&display=swap" rel="stylesheet">
<style>
  :root{
    --bg:#dcdcdc;
    --brand-blue:#1f3a93;
    --brand-red:#b3262b;
    --ink:#333;
    --muted:#666;
    --white:#fff;
    --photo-interior:linear-gradient(135deg,#8a7a68,#d9d4cc 55%,#5f5a55);
    --photo-exterior:linear-gradient(180deg,#5b9ad6 0%,#9cc3e0 40%,#6d7d84 70%,#4d7a3a 100%);
    --photo-team:linear-gradient(180deg,#f4f4f4 0%,#e6e2de 35%,#2a2a2e 70%,#1c1c20 100%);
    --photo-portrait:linear-gradient(180deg,#f2f2f2 0%,#d9d3cc 40%,#4d5058 75%,#3a3c42 100%);
  }
  *{margin:0;padding:0;box-sizing:border-box}
  html,body{width:1200px;height:581px;overflow:hidden;background:var(--bg);font-family:'Roboto',Arial,sans-serif;color:var(--ink)}
  .canvas{position:relative;width:1200px;height:581px}
  .piece{position:absolute;box-shadow:0 1px 3px rgba(0,0,0,.25)}
  .photo{position:absolute}
  .photo--interior{background:var(--photo-interior)}
  .photo--exterior{background:var(--photo-exterior)}
  .brand-name{font-family:'Roboto',Arial,sans-serif;font-weight:700;color:var(--brand-blue);white-space:nowrap}

  /* Business cards */
  .card-front{left:54px;top:270px;width:200px;height:114px;background:var(--brand-blue);color:var(--white);text-align:center}
  .card-front .brand-name{color:var(--white);font-size:16px;position:absolute;top:40px;left:0;right:0}
  .card-front .web{position:absolute;bottom:14px;left:0;right:0;font-size:5px;letter-spacing:1.5px}
  .card-back{left:54px;top:406px;width:200px;height:114px;background:var(--white)}
  .card-back .brand-name{position:absolute;left:14px;top:22px;font-size:10px}
  .card-back .person{position:absolute;left:14px;top:46px}
  .card-back .person-name{font-size:9px;font-weight:700;color:var(--brand-blue)}
  .card-back .person-role{font-size:5.5px;font-weight:500;color:var(--brand-red)}
  .card-back .details{position:absolute;left:14px;top:66px;font-size:4.6px;line-height:7px;color:var(--muted)}
  .card-back .details .ic{color:var(--brand-red)}
  .card-back .headshot{left:110px;top:8px;width:84px;height:106px;background:var(--photo-portrait)}

  /* Folder */
  .folder{position:absolute;left:293px;top:59px;width:576px;height:462px}
  .flap{position:absolute;top:0;width:21px;height:336px;background:var(--brand-red)}
  .flap--left{left:0}
  .flap--right{right:0}
  .flap-notch{position:absolute;top:200px;width:14px;height:18px;background:var(--bg);border-radius:50%}
  .flap--left .flap-notch{left:-7px}
  .flap--right .flap-notch{right:-7px}
  .folder-inside{position:absolute;left:21px;top:0;width:266px;height:336px;background:var(--brand-blue)}
  .folder-inside .p1{left:0;top:0;width:132px;height:87px}
  .folder-inside .p2{left:135px;top:0;width:131px;height:87px;background:linear-gradient(135deg,#3c4046,#a9abad 60%,#c9b23a)}
  .folder-inside .p3{left:0;top:90px;width:132px;height:86px;background:linear-gradient(135deg,#d8d8d8,#9a9a9a 60%,#efefef)}
  .folder-inside .p4{left:135px;top:90px;width:131px;height:86px;background:linear-gradient(135deg,#6b4a33,#c9a98a 50%,#9fc0d8)}
  .folder-inside .p5{left:0;top:179px;width:266px;height:157px}
  .folder-inside .contact{position:absolute;left:0;right:0;top:293px;text-align:center;font-size:6.8px;line-height:9px;color:var(--white)}
  .folder-cover{position:absolute;left:287px;top:0;width:268px;height:336px;background:var(--white)}
  .folder-cover .brand-name{position:absolute;left:0;right:0;top:66px;text-align:center;font-size:24px}
  .folder-cover .team{left:0;top:125px;width:268px;height:211px;background:var(--photo-team)}
  .pocket{position:absolute;top:336px}
  .pocket--left{left:39px}
  .pocket--right{left:289px}

  /* Postcards */
  .post-front{left:912px;top:152px;width:235px;height:177px;background:var(--photo-exterior)}
  .post-back{left:912px;top:344px;width:235px;height:177px;background:var(--white)}
  .post-back .brand-name{position:absolute;left:15px;top:28px;font-size:10px}
  .post-back .title{position:absolute;left:15px;top:59px;font-size:6.5px;font-weight:700;color:var(--brand-blue)}
  .post-back .blurb{position:absolute;left:15px;top:70px;width:86px;font-size:3.6px;line-height:5px;color:var(--muted)}
  .post-back .thumb{width:40px;height:27px}
  .post-back .t1{left:15px;top:85px;background:var(--photo-interior)}
  .post-back .t2{left:57px;top:85px;background:linear-gradient(135deg,#3c4046,#a9abad 60%,#c9b23a)}
  .post-back .t3{left:15px;top:114px;background:linear-gradient(135deg,#d8d8d8,#9a9a9a 60%,#efefef)}
  .post-back .t4{left:57px;top:114px;background:linear-gradient(135deg,#6b4a33,#c9a98a 50%,#9fc0d8)}
  .post-back .stamp{position:absolute;left:194px;top:9px;width:28px;height:28px;border:1px solid #ccc}
  .post-back .to{position:absolute;left:129px;top:46px;font-size:4.5px;color:var(--ink)}
  .post-back .address-lines{position:absolute;left:133px;top:69px;width:90px}
  .post-back .address-lines span{display:block;height:13px;border-bottom:1px solid #ddd}
  .post-back .footer{position:absolute;left:0;right:0;top:157px;text-align:center;font-size:4.5px;line-height:7px;color:var(--muted)}
  .post-back .footer b{color:var(--brand-red);font-weight:500}
</style>
</head>
<body>
<main class="canvas">

  <section class="piece card-front" aria-label="Business card front">
    <div class="brand-name">Harbrook Group</div>
    <div class="web">www.harbrookgroup.com</div>
  </section>

  <section class="piece card-back" aria-label="Business card back">
    <div class="brand-name">Harbrook Group</div>
    <div class="person">
      <div class="person-name">Daniel Reyes</div>
      <div class="person-role">CEO/Founder</div>
    </div>
    <div class="details">
      4120 Birchwood Lane<br>Juneau, Alaska 34512<br>
      <span class="ic">&#9742;</span> 555 201 4830<br>
      <span class="ic">&#9647;</span> 555 309 7214<br>
      <span class="ic">&#9993;</span> daniel@harbrookgroup.com<br>
      MLS no: 51920
    </div>
    <div class="photo headshot" role="img" aria-label="Headshot of team member in suit"></div>
  </section>

  <section class="folder" aria-label="Pocket folder">
    <div class="flap flap--left"><span class="flap-notch"></span></div>
    <div class="folder-inside">
      <div class="photo photo--interior p1" role="img" aria-label="Modern kitchen interior"></div>
      <div class="photo p2" role="img" aria-label="Living room with yellow chair"></div>
      <div class="photo p3" role="img" aria-label="Bright bathroom with glass shower"></div>
      <div class="photo p4" role="img" aria-label="Dining room with large windows"></div>
      <div class="photo photo--exterior p5" role="img" aria-label="Couple in front of a modern house"></div>
      <div class="contact">
        4120 Birchwood Lane, Juneau, Alaska 34512<br>
        P: 555 201 4830&nbsp; C: 555 309 7214&nbsp; E: daniel@harbrookgroup.com<br>
        W: www.harbrookgroup.com | MLS no: 51920
      </div>
    </div>
    <div class="folder-cover">
      <div class="brand-name">Harbrook Group</div>
      <div class="photo team" role="img" aria-label="Group photo of the real estate team"></div>
    </div>
    <div class="flap flap--right"><span class="flap-notch"></span></div>
    <svg class="pocket pocket--left" width="242" height="126" viewBox="0 0 242 126">
      <path d="M0 0H242V118Q242 126 234 126H6Q0 126 0 120V40Q0 18 0 0Z" fill="#1f3a93"/>
    </svg>
    <svg class="pocket pocket--right" width="248" height="126" viewBox="0 0 248 126">
      <path d="M0 0H248V14L236 40V118Q236 126 228 126H14Q6 126 6 118V20L0 14Z" fill="#1f3a93"/>
    </svg>
  </section>

  <section class="piece post-front" role="img" aria-label="Postcard front: couple embracing in front of a modern house"></section>

  <section class="piece post-back" aria-label="Postcard back">
    <div class="brand-name">Harbrook Group</div>
    <div class="title">Our Property</div>
    <p class="blurb">Bright family home with open kitchen, large windows and a quiet garden close to town.</p>
    <div class="photo thumb t1" role="img" aria-label="Kitchen interior"></div>
    <div class="photo thumb t2" role="img" aria-label="Living room"></div>
    <div class="photo thumb t3" role="img" aria-label="Bathroom"></div>
    <div class="photo thumb t4" role="img" aria-label="Dining room"></div>
    <div class="stamp"></div>
    <div class="to">To</div>
    <div class="address-lines"><span></span><span></span><span></span><span></span></div>
    <div class="footer">
      4120 Birchwood Lane, Juneau, Alaska 34512 | <b>P:</b> 555 201 4830<br>
      <b>C:</b> 555 309 7214 <b>E:</b> daniel@harbrookgroup.com <b>W:</b> www.harbrookgroup.com | MLS no: 51920
    </div>
  </section>

</main>
</body>
</html>
```